my website is toncielbrode.com. (brand name is ton ciel brodé) This is just a template that i have choose for. The content and the pictures are not about my business just the template.
I would like to have 4 pages for now. 1 homepage, which will be an overview for all pages, it is right now in this way. It will directly highlight my story. My website will tell an exclusive story about details which makes the difference and will make people happy with very small things. It will be art related but very stylish as well. I also want to have a event agenda on my homepage where people can see where my next event is. Page 2 my blog, where I will write weekly about mindset, lifestyle and details. Inspiration place for people who are looking for unique and exclusive approaches in life. Page 3 shop, where I will sell my stuff which is handmade and unique, it will be limited edition stuff. Mostly I will make the designs from marbling art, which I am a teacher for. (https://www.vidorama-example.com/watch?v=Xk3pQr7LmZa) check this video out for more. Page 4 is book page. Here people will be able to book private or group classes for marbling art (check the video). I have already a community of more than 500 people on join nest, which will be my public as well. I wanna implement the join nest button on this page as well. to be able to track.

This is about my website. I also need a logo for my brand, which will suit my website and my goals.

I can also give you a reference website, which really like as structure and style;
https://www.brightmorrowgoods-example.com/products/the-quiet-ledger?gclid=Zx8RtYpWq2LmN4vBcD6sKjH3gFaE9uIoP1lKzXcVbNm7QwErTyUiOp0AsDfGhJkLzXcVbNm5Qw2ErTyUi_oPaSd8FgHjKlZxC_vbNQ

ton ciel brodé

4 page

• I can also give you a reference website, which really like as structure and style;
• https://www.brightmorrowgoods-example.com/products/the-quiet-ledger?gclid=Zx8RtYpWq2LmN4vBcD6sKjH3gFaE9uIoP1lKzXcVbNm7QwErTyUiOp0AsDfGhJkLzXcVbNm5Qw2ErTyUi_oPaSd8FgHjKlZxC_vbNQ

```html
<!DOCTYPE html>
<html lang="en">
<head>
<meta charset="utf-8">
<title>ton ciel brodé — Home</title>
<link href="https://fonts.googleapis.com/css2?family=Josefin+Sans:wght@400;600&family=Playfair+Display:wght@700;900&family=Yesteryear&display=swap" rel="stylesheet">
<style>
:root{
  --ink:#111111;
  --paper:#ffffff;
  --card:#f3efec;
  --dark:#262626;
  --muted:#cfcfcf;
  --band:#ededed;
}
*{box-sizing:border-box;margin:0;padding:0}
html,body{width:1200px;height:1200px;overflow:hidden;background:var(--paper);color:var(--ink)}
body{position:relative;font-family:"Josefin Sans",sans-serif}
.site-header{position:absolute;left:0;top:0;width:1200px;height:83px;background:var(--paper);z-index:5}
.nav-link{position:absolute;top:33px;font-size:15px;letter-spacing:2px;color:var(--ink);text-decoration:none}
.nav-link.is-active{border-bottom:1px solid var(--muted);padding-bottom:3px}
.brand{position:absolute;left:536px;top:26px;display:flex;align-items:center;gap:8px;font-family:"Josefin Sans",sans-serif;font-size:18px;font-weight:600;color:var(--ink);text-decoration:none}
.brand-mark{width:12px;height:12px;border:1.5px solid var(--ink);border-radius:50%}
.social{position:absolute;top:32px;width:13px;height:13px;border:1.5px solid var(--ink);border-radius:50%}
.cart{position:absolute;left:1062px;top:24px}
.hero-art{position:absolute;left:562px;top:83px;width:638px;height:517px;background:linear-gradient(160deg,#c0a062 0%,#b54a3c 20%,#3c6a3a 42%,#2c4a6c 55%,#7a5a88 72%,#c9c1c6 85%,#5c2a30 100%)}
.hero-photo{position:absolute;left:0;top:83px;width:638px;height:449px;background:linear-gradient(120deg,#5d5b58 0%,#7a7874 45%,#8f8d8a 70%,#bdbdbd 100%);box-shadow:0 8px 14px rgba(0,0,0,.18);z-index:1}
.hero-card{position:absolute;left:302px;top:207px;width:596px;height:253px;background:var(--paper);z-index:2;text-align:center}
.hero-kicker{position:absolute;left:0;right:0;top:20px;font-family:"Yesteryear",cursive;font-size:40px;line-height:1}
.hero-title{position:absolute;left:0;right:0;top:60px;font-family:"Yesteryear",cursive;font-size:62px;font-weight:400;line-height:1}
.hero-text{position:absolute;left:22px;right:22px;top:122px;font-size:13.5px;line-height:19.5px}
.hero-cta{position:absolute;left:0;right:0;top:213px;font-size:18px;color:var(--ink);text-decoration:none}
.products{position:absolute;left:0;top:640px;width:1200px;height:440px;overflow:hidden}
.product{position:absolute;top:36px;width:238px;height:378px}
.product.is-featured{background:var(--paper);box-shadow:0 4px 16px rgba(0,0,0,.12)}
.product-name{position:absolute;left:22px;top:57px;font-family:"Playfair Display",serif;font-weight:900;font-size:19px;white-space:nowrap}
.product-card{position:absolute;left:0;top:133px;width:238px;height:245px;background:var(--card)}
.product-image{position:absolute;left:70px;top:60px;width:98px;height:98px;background:linear-gradient(#ebe5e1,#e2dbd6)}
.product-go{position:absolute;left:181px;top:112px;width:42px;height:42px;background:var(--ink);display:flex;align-items:center;justify-content:center}
.badge{position:absolute;left:0;top:0;width:96px;height:28px;background:var(--dark);color:var(--paper);font-size:13px;display:flex;align-items:center;justify-content:center}
.price{position:absolute;left:117px;top:203px;width:106px;height:28px;background:var(--dark);color:var(--paper);font-size:13.5px;display:flex;align-items:center;justify-content:center}
.quick-view{position:absolute;left:0;top:104px;width:238px;height:38px;background:rgba(255,255,255,.88);font-size:17px;display:flex;align-items:center;justify-content:center}
.pager{position:absolute;left:0;top:982px;width:300px;height:40px;font-weight:600;font-size:15px}
.pager-line{position:absolute;left:0;top:20px;width:120px;height:1px;background:var(--muted)}
.pager-current{position:absolute;left:119px;top:4px;width:32px;height:32px;border:1px solid #e2e2e2;border-radius:50%;background:var(--paper);display:flex;align-items:center;justify-content:center}
.pager-num{position:absolute;top:12px}
.pager-dash{position:absolute;top:19px;height:2px;background:var(--ink)}
.footer-band{position:absolute;left:0;top:1130px;width:1200px;height:70px;background:linear-gradient(90deg,#e8e8e8,#f0f0f0 40%,#e9e9e9)}
</style>
</head>
<body>
<header class="site-header">
  <a class="nav-link is-active" href="#" style="left:244px">Home</a>
  <a class="nav-link" href="#" style="left:369px">Shop</a>
  <a class="brand" href="#"><span class="brand-mark"></span>ton ciel brodé</a>
  <a class="nav-link" href="#" style="left:738px">Book Online</a>
  <a class="nav-link" href="#" style="left:917px">Blog</a>
  <a class="social" href="#" aria-label="Social link" style="left:1006px"></a>
  <a class="social" href="#" aria-label="Social link" style="left:1032px"></a>
  <svg class="cart" width="26" height="28" viewBox="0 0 26 28" aria-label="Cart">
    <path d="M1 6h4l3 12h13l3-9H7" fill="none" stroke="#111" stroke-width="1.3"/>
    <circle cx="10" cy="23" r="1.6" fill="none" stroke="#111"/><circle cx="19" cy="23" r="1.6" fill="none" stroke="#111"/>
    <circle cx="16" cy="7" r="5" fill="#fff" stroke="#111"/><text x="16" y="9.5" font-size="7" text-anchor="middle" font-family="Josefin Sans,sans-serif">0</text>
  </svg>
</header>

<div class="hero-art" role="img" aria-label="Marbling paint swirls with brushes"></div>
<div class="hero-photo" role="img" aria-label="Man in denim shirt beside a white plinth"></div>
<section class="hero-card">
  <p class="hero-kicker">Our New</p>
  <h1 class="hero-title">Arrivals Are Here</h1>
  <p class="hero-text">ton ciel brodé is a leading Online Store. We provide an unparalleled selection of the very best quality products, an easy and comfortable shopping experience, expedited shipping offers, and exceptional customer service. Check out our collection of new arrivals, best-sellers, and clearance items today.</p>
  <a class="hero-cta" href="#">Shop Now »</a>
</section>

<section class="products">
  <article class="product" style="left:310px">
    <h2 class="product-name">I'm a Product</h2>
    <div class="product-card">
      <div class="product-image" role="img" aria-label="Line drawing of a shirt"></div>
      <span class="badge">Best Seller</span>
      <span class="price">€ 10.00</span>
    </div>
    <a class="product-go" href="#"><svg width="10" height="12"><path d="M3 1l5 5-5 5" fill="none" stroke="#fff" stroke-width="1.4"/></svg></a>
  </article>
  <article class="product is-featured" style="left:572px">
    <h2 class="product-name">I' m a Product</h2>
    <div class="product-card">
      <div class="product-image" role="img" aria-label="Line drawing of a backpack"></div>
      <span class="quick-view">Quick View</span>
      <span class="price">€ 15.00</span>
    </div>
    <a class="product-go" href="#"><svg width="10" height="12"><path d="M3 1l5 5-5 5" fill="none" stroke="#fff" stroke-width="1.4"/></svg></a>
  </article>
  <article class="product" style="left:834px">
    <h2 class="product-name">I' m a Product</h2>
    <div class="product-card">
      <div class="product-image" role="img" aria-label="Line drawing of a tank top"></div>
      <span class="badge">New</span>
      <span class="price">€ 120.00</span>
    </div>
    <a class="product-go" href="#"><svg width="10" height="12"><path d="M3 1l5 5-5 5" fill="none" stroke="#fff" stroke-width="1.4"/></svg></a>
  </article>
  <article class="product" style="left:1096px">
    <h2 class="product-name">I' m a Product</h2>
    <div class="product-card">
      <div class="product-image" role="img" aria-label="Line drawing of a shoe" style="left:0"></div>
    </div>
  </article>
</section>

<nav class="pager" aria-label="Pages">
  <span class="pager-line"></span>
  <span class="pager-current">1</span>
  <span class="pager-num" style="left:166px">2</span>
  <span class="pager-num" style="left:193px">3</span>
  <span class="pager-dash" style="left:218px;width:38px"></span>
  <span class="pager-dash" style="left:261px;width:11px"></span>
</nav>

<div class="footer-band" role="img" aria-label="Faint photo of an artist's workspace"></div>
</body>
</html>
```